We need a business card design for our website qvwtrading.net. The Star Headline is qvwtrading.net, in large lettering.We sell fashion rings of titanium, mirror pollished stainless steel, and related jewelry. Basically quality products competing with the high expense of gold.We have to portray honesty and trust, because thats who I am. I know marketing, but I am weak on colors and layout. 3D Gold curved edge letters are ok. No green and yellow.Black,Red,Purple and White in small amounts.No fancy Lettering.
No Rainbows in printing.
Our goal is selling our products online globally

Kind Regards Maren Tulloch

Fashion

qvwtrading.net
known for our ideal fit rings
email.marentullochptyltd@corvexmail com

```html
<!DOCTYPE html>
<html lang="en">
<head>
<meta charset="utf-8">
<title>qvwtrading.net business cards</title>
<link rel="stylesheet" href="https://fonts.googleapis.com/css2?family=Fredoka:wght@500;600&display=swap">
<style>
  :root {
    --backdrop: #5b5b5c;
    --paper: #ffffff;
    --brand-blue: #1877c0;
    --deep-blue: #1a6fb8;
    --brand-purple: #8c2a91;
    --brand-yellow: #f5e21c;
    --ink: #333333;
    --charcoal: #414042;
    --mid-grey: #8a8a8a;
    --white: #ffffff;
  }
  * { box-sizing: border-box; margin: 0; padding: 0; }
  html, body { width: 1200px; height: 1028px; overflow: hidden; }
  body {
    background: var(--backdrop);
    position: relative;
    font-family: "Fredoka", "Arial Rounded MT Bold", sans-serif;
  }
  .card {
    position: absolute;
    width: 558px;
    height: 343px;
    overflow: hidden;
    box-shadow: 0 3px 10px rgba(0,0,0,.45);
  }
  .card--front { background: var(--paper); }
  .card--back-blue { background: var(--brand-blue); }
  .card--back-dark { background: var(--charcoal); }
  .card-art { position: absolute; inset: 0; width: 558px; height: 343px; }

  .headline {
    position: absolute;
    left: 18px;
    top: 80px;
    font-size: 44px;
    font-weight: 600;
    letter-spacing: -0.5px;
    line-height: 1;
  }
  .tagline {
    position: absolute;
    left: 57px;
    top: 140px;
    font-size: 16px;
    font-weight: 500;
    color: var(--ink);
    letter-spacing: 0.3px;
  }
  .contact {
    position: absolute;
    left: 23px;
    top: 300px;
    display: flex;
    align-items: center;
    gap: 8px;
    font-family: "Fredoka", Arial, sans-serif;
    font-weight: 500;
    font-size: 13px;
    letter-spacing: 1px;
    color: var(--white);
  }
  .contact svg { width: 14px; height: 11px; }
  .brand-mark {
    position: absolute;
    right: 22px;
    top: 286px;
    font-size: 33px;
    font-weight: 600;
    line-height: 1;
  }
  .back-name {
    position: absolute;
    right: 28px;
    top: 262px;
    font-size: 47px;
    font-weight: 600;
    line-height: 1;
  }
  .is-yellow { color: var(--brand-yellow); }
  .is-charcoal { color: var(--charcoal); }
  .is-white { color: var(--white); }
</style>
</head>
<body>

<!-- Front, colour -->
<section class="card card--front" style="left:22px; top:130px;">
  <svg class="card-art" viewBox="0 0 558 343">
    <path d="M0,252 C110,234 240,236 318,259 C230,250 110,258 0,278 Z" fill="var(--brand-purple)"/>
    <path d="M0,278 C120,259 250,254 330,262 C420,270 500,256 558,228 L558,343 L0,343 Z" fill="var(--brand-blue)"/>

    <g transform="translate(451,103) rotate(-20)">
      <rect x="-66" y="-66" width="132" height="132" fill="var(--brand-blue)" opacity=".45"/>
      <rect x="-62" y="-62" width="124" height="124" fill="var(--brand-purple)" opacity=".45" transform="rotate(12)"/>
    </g>
    <g transform="translate(451,105) rotate(-12)">
      <rect x="-55" y="-55" width="110" height="110" fill="var(--deep-blue)"/>
      <rect x="-49" y="-49" width="98" height="98" fill="var(--white)"/>
      <rect x="-44" y="-44" width="88" height="88" fill="#d9dde1" role="img" aria-label="Photo of a pair of polished steel rings"/>
    </g>

    <g transform="translate(396,170) rotate(-22)">
      <rect x="-46" y="-46" width="92" height="92" fill="var(--brand-purple)" opacity=".45"/>
      <rect x="-42" y="-42" width="84" height="84" fill="var(--brand-blue)" opacity=".45" transform="rotate(14)"/>
      <rect x="-36" y="-36" width="72" height="72" fill="var(--deep-blue)"/>
      <rect x="-31" y="-31" width="62" height="62" fill="var(--white)"/>
      <rect x="-27" y="-27" width="54" height="54" fill="#d8c8a0" role="img" aria-label="Photo of a gold and steel ring"/>
    </g>

    <g transform="translate(475,222) rotate(-22)">
      <rect x="-52" y="-52" width="104" height="104" fill="var(--brand-purple)" opacity=".45"/>
      <rect x="-48" y="-48" width="96" height="96" fill="var(--brand-blue)" opacity=".45" transform="rotate(14)"/>
      <rect x="-42" y="-42" width="84" height="84" fill="var(--deep-blue)"/>
      <rect x="-37" y="-37" width="74" height="74" fill="var(--white)"/>
      <rect x="-32" y="-32" width="64" height="64" fill="#b9bcc0" role="img" aria-label="Photo of a black and steel ring"/>
    </g>
  </svg>
  <h1 class="headline is-yellow">qvwtrading.net</h1>
  <p class="tagline">Known For Our Ideal Fit Rings</p>
  <p class="contact">
    <svg viewBox="0 0 14 11"><rect x="0.5" y="0.5" width="13" height="10" fill="var(--white)"/><path d="M1,1.5 L7,6 L13,1.5" fill="none" stroke="var(--brand-blue)" stroke-width="1.3"/></svg>
    marentullochptyltd@corvexmail.com
  </p>
  <p class="brand-mark is-yellow">Qvwtrading</p>
</section>

<!-- Back, blue -->
<section class="card card--back-blue" style="left:620px; top:130px;">
  <p class="back-name is-yellow">qvwtrading.net</p>
</section>

<!-- Front, mono -->
<section class="card card--front" style="left:22px; top:553px;">
  <svg class="card-art" viewBox="0 0 558 343">
    <path d="M0,252 C110,234 240,236 318,259 C230,250 110,258 0,278 Z" fill="var(--mid-grey)"/>
    <path d="M0,278 C120,259 250,254 330,262 C420,270 500,256 558,228 L558,343 L0,343 Z" fill="var(--charcoal)"/>

    <g transform="translate(451,103) rotate(-20)">
      <rect x="-66" y="-66" width="132" height="132" fill="#777" opacity=".45"/>
      <rect x="-62" y="-62" width="124" height="124" fill="#555" opacity=".45" transform="rotate(12)"/>
    </g>
    <g transform="translate(451,105) rotate(-12)">
      <rect x="-55" y="-55" width="110" height="110" fill="var(--charcoal)"/>
      <rect x="-49" y="-49" width="98" height="98" fill="var(--white)"/>
      <rect x="-44" y="-44" width="88" height="88" fill="#dcdcdc" role="img" aria-label="Photo of a pair of polished steel rings"/>
    </g>

    <g transform="translate(396,170) rotate(-22)">
      <rect x="-46" y="-46" width="92" height="92" fill="#666" opacity=".45"/>
      <rect x="-42" y="-42" width="84" height="84" fill="#888" opacity=".45" transform="rotate(14)"/>
      <rect x="-36" y="-36" width="72" height="72" fill="var(--charcoal)"/>
      <rect x="-31" y="-31" width="62" height="62" fill="var(--white)"/>
      <rect x="-27" y="-27" width="54" height="54" fill="#d8c8a0" role="img" aria-label="Photo of a gold and steel ring"/>
    </g>

    <g transform="translate(475,222) rotate(-22)">
      <rect x="-52" y="-52" width="104" height="104" fill="#666" opacity=".45"/>
      <rect x="-48" y="-48" width="96" height="96" fill="#888" opacity=".45" transform="rotate(14)"/>
      <rect x="-42" y="-42" width="84" height="84" fill="var(--charcoal)"/>
      <rect x="-37" y="-37" width="74" height="74" fill="var(--white)"/>
      <rect x="-32" y="-32" width="64" height="64" fill="#b9bcc0" role="img" aria-label="Photo of a black and steel ring"/>
    </g>
  </svg>
  <h2 class="headline is-charcoal">qvwtrading.net</h2>
  <p class="tagline">Known For Our Ideal Fit Rings</p>
  <p class="contact">
    <svg viewBox="0 0 14 11"><rect x="0.5" y="0.5" width="13" height="10" fill="var(--white)"/><path d="M1,1.5 L7,6 L13,1.5" fill="none" stroke="var(--charcoal)" stroke-width="1.3"/></svg>
    marentullochptyltd@corvexmail.com
  </p>
  <p class="brand-mark is-white">Qvwtrading</p>
</section>

<!-- Back, charcoal -->
<section class="card card--back-dark" style="left:620px; top:553px;">
  <p class="back-name is-white">qvwtrading.net</p>
</section>

</body>
</html>
```